Local Mortgage Broker requires DL Flyer

I Require DL sized design for local mortgage broker. Content that will go on the flyer is attached along with the logo.
Looking for a bright & catchy design with that little OOMPH.....on the creative side.
Am looking for a responsive campaign with this style of marketing. The main message is that "We may be able to save thousands of dollars for you, just give us a chance to review your mortgages"

Target Market(s)

All home owners with a mortgage or eople looking to buy their first home.

Industry/Entity Type

Marketing

```html
<!DOCTYPE html>
<html lang="en">
<head>
<meta charset="utf-8">
<title>HomeWise Lending – DL Flyer</title>
<link rel="stylesheet" href="https://fonts.googleapis.com/css2?family=Roboto+Condensed:wght@700;800;900&family=Arimo:wght@400;700&display=swap">
<style>
  :root {
    --backdrop: #6b6c70;
    --paper: #ffffff;
    --navy: #2b2862;
    --red: #d4202a;
    --grey-text: #6d6e71;
    --grey-soft: #d9d9de;
    --badge-grey: #6d6e71;
    --shadow-grey: #c9c9cc;
    --ink: #1d1d1f;
    --photo-top: #dcd9d6;
    --photo-mid: #ebe9e7;
  }
  * { margin: 0; padding: 0; box-sizing: border-box; }
  html, body { width: 1200px; height: 2264px; overflow: hidden; }
  body { background: var(--backdrop); position: relative; font-family: "Arimo", Arial, sans-serif; }

  .flyer {
    position: absolute; left: 117px; top: 117px;
    width: 966px; height: 2030px;
    background: var(--paper); overflow: hidden;
  }

  .hero-photo {
    position: absolute; left: 0; top: 0; width: 966px; height: 510px;
    background: linear-gradient(180deg, var(--photo-top) 0%, var(--photo-mid) 50%, var(--paper) 100%);
  }

  .offer-lead {
    position: absolute; left: 87px; top: 520px;
    font-family: "Roboto Condensed", Arial, sans-serif; font-weight: 800;
    font-size: 50px; color: var(--navy);
  }
  .offer-amount {
    position: absolute; left: 62px; top: 558px; width: 860px;
    font-family: "Roboto Condensed", Arial, sans-serif; font-weight: 900;
    font-size: 318px; line-height: 1; letter-spacing: -4px;
    color: var(--red);
    text-shadow: 10px 8px 0 var(--shadow-grey);
  }
  .offer-conditions {
    position: absolute; right: 118px; top: 858px;
    font-size: 24px; color: var(--grey-text);
  }
  .offer-conditions sup { font-size: 28px; }

  .headline {
    position: absolute; left: 0; top: 918px; width: 966px;
    text-align: center;
    font-family: "Roboto Condensed", Arial, sans-serif; font-weight: 900;
    font-size: 96px; line-height: 88px; color: var(--navy);
  }
  .subline {
    position: absolute; left: 0; top: 1128px; width: 966px;
    text-align: center; font-weight: 700;
    font-size: 36px; line-height: 42px; color: var(--grey-text);
  }

  .brand {
    position: absolute; left: 104px; top: 1428px;
    display: flex; align-items: center; gap: 16px;
  }
  .brand-square { width: 36px; height: 36px; background: var(--navy); }
  .brand-name {
    font-weight: 700; font-size: 46px; line-height: 56px;
    color: var(--navy); white-space: nowrap;
  }

  .call-badge {
    position: absolute; left: 657px; top: 1298px;
    width: 242px; height: 242px; border-radius: 50%;
    background: var(--badge-grey);
    display: flex; align-items: center; justify-content: center;
  }
  .call-badge span {
    display: block; transform: rotate(20deg);
    text-align: center; color: var(--paper);
    font-size: 48px; line-height: 52px;
  }

  .contact-band {
    position: absolute; left: 0; top: 1553px; width: 966px; height: 223px;
    background: var(--navy); text-align: center;
  }
  .contact-phone {
    display: block; padding-top: 20px;
    font-family: "Roboto Condensed", Arial, sans-serif; font-weight: 700;
    font-size: 128px; line-height: 124px; color: var(--grey-soft);
  }
  .contact-web {
    display: block;
    font-family: "Roboto Condensed", Arial, sans-serif; font-weight: 700;
    font-size: 56px; line-height: 62px; color: var(--paper);
  }

  .fine-print {
    position: absolute; left: 0; top: 1796px; width: 966px;
    text-align: center; font-size: 31px; line-height: 39px; color: var(--ink);
  }
</style>
</head>
<body>
  <main class="flyer">
    <div class="hero-photo" role="img" aria-label="Photo of a hand signing mortgage papers beside a small model house and a set of keys"></div>

    <div class="offer-lead">Upto</div>
    <div class="offer-amount">$3000</div>
    <div class="offer-conditions">conditions apply.<sup>*</sup></div>

    <h1 class="headline">GET REWARDED BY<br>SWITCHING OVER.</h1>
    <p class="subline">GET UP TO $3000 VOUCHER OR CASH BACK*<br>ON THE SETTLEMENT OF YOUR LOAN.</p>

    <div class="brand">
      <span class="brand-square"></span>
      <span class="brand-name">HomeWise Lending</span>
    </div>

    <div class="call-badge"><span>CALL<br>NOW!</span></div>

    <section class="contact-band">
      <span class="contact-phone">0400 555 018</span>
      <span class="contact-web">www.homewiselending.com.au</span>
    </section>

    <p class="fine-print">
      *based on the size of the loan, You get upto 0.3%<br>
      of your total loan settled through us.<br>
      For example a refinance of <b>$600,000</b> mortgage to any of<br>
      our panel lenders will get you <b>$ 0.30%</b> of the $600,000,<br>
      which is <b>$1,800</b> as your bonus/ reward,
    </p>
  </main>
</body>
</html>
```